new packages design wanted for a chip wagon business

We are a chip wagon business . our menu is simple , hot dogs, french fries, hamburgers, drinks and ice cream!

All Burgers are served with a mix of traditional French Fries and Sweet Potato Fries!

Ice Creams started with the slogan “Life is uncertain, eat dessert first” which represented a strategic approach to the enjoyment of life.

Industry/Entity Type

Business

Font styles to use
Serif
Sans Serif

Colors
0492cd
e667a6
33b8a4
86cfc6

```html
<!DOCTYPE html>
<html lang="en">
<head>
<meta charset="utf-8">
<title>Curbside Chips – Menu Leaflet</title>
<link href="https://fonts.googleapis.com/css2?family=Oswald:wght@700&family=Questrial&display=swap" rel="stylesheet">
<style>
:root{
  --stage:#e6e7e9;
  --brand-blue:#0492cd;
  --deep-blue:#02557f;
  --ice:#b9cfdf;
  --ice-light:#cfdfea;
  --menu-bg:#9cc3db;
  --menu-frame:#b4d3e6;
  --bar:#7fbfe0;
  --bar-dark:#6cb3d8;
  --teal:#33b8a4;
  --mint:#86cfc6;
  --pink:#e667a6;
  --ink:#1a1a1a;
  --cream:#fde3cc;
  --white:#ffffff;
}
*{margin:0;padding:0;box-sizing:border-box}
html,body{width:1200px;height:863px;overflow:hidden;background:var(--stage)}
.stage{position:absolute;left:0;top:0;width:1491px;height:1072px;transform:scale(.8048);transform-origin:0 0;font-family:"Questrial",sans-serif}
.page{position:absolute;top:162px;width:529px;height:748px;overflow:hidden}
.cover{left:195px;background:var(--ice)}
.cover svg{position:absolute;left:0;top:0}
.brand{position:absolute;left:30px;top:128px;font-size:30px;color:var(--teal);letter-spacing:1px;display:flex;align-items:center;gap:10px}
.brand .mark{width:16px;height:16px;background:var(--pink)}
.food-art{position:absolute;border-radius:50%}
.food-art.main{left:95px;top:205px;width:340px;height:340px;border:9px solid var(--brand-blue);background:radial-gradient(circle at 55% 45%,#f28c2a 0 28%,#f6c431 29% 42%,var(--cream) 43%)}
.food-art.dessert{left:108px;top:442px;width:148px;height:148px;border:6px solid var(--mint);background:radial-gradient(circle at 40% 45%,#f08a7a 0 22%,#f5c542 23% 34%,#f4f0ea 35%)}
.cover-note{position:absolute;left:0;top:676px;width:529px;height:46px;background:var(--deep-blue);clip-path:polygon(0 0,88% 0,100% 100%,0 100%);color:var(--white);padding:8px 0 0 53px}
.cover-note .lead{font-size:19px;line-height:1}
.cover-note .small{font-size:9px;margin-top:5px}
.menu{left:767px;background:var(--menu-bg)}
.menu-frame{position:absolute;left:25px;top:25px;width:479px;height:698px;background:var(--menu-frame);opacity:.75}
.menu-title{position:absolute;left:55px;top:75px;width:418px;height:55px;background:var(--bar);display:flex;align-items:center;justify-content:center;font-family:"Oswald",sans-serif;font-weight:700;font-size:28px;color:var(--ink);letter-spacing:.5px}
.menu-item{position:absolute;left:45px;width:439px;height:69px}
.menu-item .icon-tile{position:absolute;left:0;top:0;width:102px;height:69px;border-radius:16px;background:var(--bar-dark);display:flex;align-items:center;justify-content:center}
.menu-item .icon-art{width:56px;height:46px;border-radius:40%}
.menu-item .bar{position:absolute;left:115px;top:0;width:324px;height:69px;background:var(--bar-dark);display:flex;align-items:center;padding-left:31px}
.menu-item .name{font-size:31px;color:var(--ink)}
.menu-item .note{font-size:13px;line-height:18px;color:var(--ink);margin-left:8px}
.menu-item .note.right{position:absolute;right:18px;text-align:center}
.brand.small{left:408px;top:680px;font-size:15px;gap:5px}
.brand.small .mark{width:8px;height:8px}
</style>
</head>
<body>
<main class="stage">
  <section class="page cover">
    <svg width="529" height="748" viewBox="0 0 529 748" aria-hidden="true">
      <path d="M0 0H529V280C470 190 360 120 235 118Z" fill="var(--brand-blue)"/>
      <path d="M0 468C60 470 40 560 100 600C160 640 240 625 300 640C400 665 470 700 529 748H0Z" fill="var(--brand-blue)"/>
      <path d="M0 0L235 118C200 118 180 150 160 190L0 250Z" fill="var(--ice-light)" opacity=".5"/>
    </svg>
    <div class="brand"><span class="mark"></span>Curbside Chips</div>
    <div class="food-art main" role="img" aria-label="Illustration of a burger, fries and a hot dog"></div>
    <div class="food-art dessert" role="img" aria-label="Illustration of an ice cream sundae and a mug of drink"></div>
    <div class="cover-note">
      <p class="lead">All Burgers are served with a</p>
      <p class="small">mix of traditional French Fries and Sweet Potato Fries!</p>
    </div>
  </section>

  <section class="page menu">
    <div class="menu-frame"></div>
    <h1 class="menu-title">FOOD MENU</h1>
    <div class="menu-item" style="top:204px">
      <div class="icon-tile"><div class="icon-art" role="img" aria-label="Hot dog icon" style="background:#e9833a"></div></div>
      <div class="bar"><span class="name">Hot Dogs</span></div>
    </div>
    <div class="menu-item" style="top:286px">
      <div class="icon-tile"><div class="icon-art" role="img" aria-label="French fries icon" style="background:#f3c52f"></div></div>
      <div class="bar"><span class="name">French Fries</span></div>
    </div>
    <div class="menu-item" style="top:369px">
      <div class="icon-tile"><div class="icon-art" role="img" aria-label="Hamburger icon" style="background:#f08a2c"></div></div>
      <div class="bar"><span class="name">Hamburgers</span><span class="note">French Fries and<br>Sweet Potato Fries</span></div>
    </div>
    <div class="menu-item" style="top:452px">
      <div class="icon-tile"><div class="icon-art" role="img" aria-label="Drink mug icon" style="background:#f5c542"></div></div>
      <div class="bar"><span class="name">Drinks</span></div>
    </div>
    <div class="menu-item" style="top:534px">
      <div class="icon-tile"><div class="icon-art" role="img" aria-label="Ice cream sundae icon" style="background:#f08a7a"></div></div>
      <div class="bar"><span class="name">Ice Cream</span><span class="note right">Life is uncertain,<br>eat dessert first</span></div>
    </div>
    <div class="brand small"><span class="mark"></span>Curbside Chips</div>
  </section>
</main>
</body>
</html>
```